Email Template for AI Website Builder Marketing Campaign

Update: All the designs submitted have too much content for an email template. I have attached a mockup example of a simplified design. Please follow this guideline to revise your design to be less "wordy" and have less content to optimize the delivery rate of the emails. I have also attached the images I used to create the mockup. Feel free to use these images for your revised designs.
Original Brief:
I need a catchy email template for my new AI Website Builder, WebQuilt.ai. The template must be professional, colorful, yet not too complex. The concept of the product is this:
WebQuilt uses Artificial Intelligence (AI) to instantly build stunning websites, absolutely FREE. The user simply specifies their business name and business category (industry), and their stunning new website appears before their eyes!
The template will be used in MailChimp, so please provide the code that I can simply paste into the email body.
Here is a screenshot of our new website (which is not online yet) so you can match the color scheme and style of the email template to the new website design:
https://pixbinstore.com/art_img/7310582/2208634/48165027/9qrt41hwk826zlmpb3nqd7wyex_image.jpg
Let me know if you have any questions.
Thanks!
All submitted designs are too lengthy (too much content) for an email template. I will provide a mockup showing a sample of how you can simplify your design to function better as an email template and better suit my needs. I appreciate your patience!

```html
<!DOCTYPE html>
<html lang="en">
<head>
<meta charset="utf-8">
<title>WebQuilt Email</title>
<link href="https://fonts.googleapis.com/css2?family=Poppins:wght@400;500;600;700&display=swap" rel="stylesheet">
<style>
:root{
  --page:#f5f5f5;
  --white:#ffffff;
  --ink:#1c1c1c;
  --muted:#444;
  --accent:#1a9cf0;
  --cyan:#2ad4f5;
  --btn-a:#36d3f3;
  --btn-b:#1a9af7;
  --footer-a:#0b0d50;
  --footer-b:#23144a;
  --footer-text:#a9a7c4;
}
*{margin:0;padding:0;box-sizing:border-box}
html,body{width:959px;height:1200px;overflow:hidden;background:var(--page)}
body{font-family:"Poppins",sans-serif}
.stage{position:absolute;left:0;top:0;width:1132px;height:1416px;transform:scale(0.84717);transform-origin:0 0}
.email{position:absolute;left:264px;top:117px;width:603px;height:1182px;background:var(--white);box-shadow:0 0 6px rgba(0,0,0,.05)}
.hero{position:absolute;left:0;top:0;width:600px;height:560px;overflow:hidden;
  background:radial-gradient(circle at 45% 45%,#3b8fd6 0%,#2a5aae 30%,transparent 60%),
  linear-gradient(160deg,#3a1f7a 0%,#2d3d9a 35%,#2a5bb0 60%,#1b2e6e 100%)}
.hero-photo{position:absolute;inset:0;background:radial-gradient(ellipse at 85% 40%,rgba(200,210,240,.45),transparent 35%),radial-gradient(ellipse at 40% 80%,rgba(20,30,80,.55),transparent 50%)}
.brand{position:absolute;display:flex;align-items:center;gap:8px;color:var(--white);font-weight:500}
.brand-mark{width:16px;height:16px;border-radius:3px;background:var(--cyan)}
.hero .brand{left:38px;top:20px;font-size:21px}
.nav{position:absolute;right:38px;top:27px;display:flex;gap:26px;font-size:11px;font-weight:500;color:#cfd3ef}
.headline{position:absolute;left:38px;top:101px;color:var(--white);font-size:29px;line-height:47px;font-weight:400}
.headline b{font-weight:700}
.btn{position:absolute;display:flex;align-items:center;justify-content:center;height:44px;width:175px;border-radius:3px;
  background:linear-gradient(90deg,var(--btn-a),var(--btn-b));color:var(--white);font-size:10.5px;font-weight:600;text-transform:uppercase}
.hero .btn{left:38px;top:262px}
.wave{position:absolute;left:0;top:500px;width:600px;height:62px}
.intro{position:absolute;left:0;top:570px;width:600px;text-align:center}
.eyebrow{color:var(--accent);font-weight:700;font-size:16px}
.intro h1{margin-top:12px;font-size:25px;line-height:36px;font-weight:700;color:var(--ink)}
.illustration{position:absolute;left:32px;top:698px;width:264px;height:186px;border-radius:8px;
  background:linear-gradient(135deg,#eef4fb,#dcebf8)}
.copy{position:absolute;left:321px;top:718px;width:252px;font-size:12px;line-height:20px;color:var(--muted)}
.copy p+p{margin-top:20px}
.email > .btn{left:215px;top:917px;z-index:2}
.footer{position:absolute;left:3px;top:941px;width:600px;height:241px;background:linear-gradient(180deg,var(--footer-a),var(--footer-b));text-align:center}
.footer .brand{left:50%;transform:translateX(-50%);top:52px;font-size:23px}
.tagline{position:absolute;top:98px;width:100%;font-size:12px;color:var(--footer-text)}
.social{position:absolute;top:131px;left:244px;display:flex;gap:7px}
.social span{width:22px;height:22px;border:1.3px solid var(--footer-text);border-radius:50%}
.rule{position:absolute;left:36px;right:36px;top:176px;height:1px;background:rgba(255,255,255,.15)}
.legal{position:absolute;left:38px;right:36px;top:198px;display:flex;justify-content:space-between;font-size:14px;color:var(--footer-text)}
</style>
</head>
<body>
<div class="stage">
  <div class="email">
    <header class="hero">
      <div class="hero-photo" role="img" aria-label="Photo of a humanoid robot typing on a laptop in front of a glowing digital globe"></div>
      <div class="brand"><span class="brand-mark"></span>WebQuilt</div>
      <nav class="nav"><span>About</span><span>Learn</span><span>History</span><span>Contact</span></nav>
      <h2 class="headline">Your <b>FREE</b> Stunning Website<br>in <b>1-Click Build</b><br>By <b>Artificial Intelligence</b></h2>
      <a class="btn">Build my free website</a>
      <svg class="wave" viewBox="0 0 600 62" preserveAspectRatio="none">
        <path d="M0 52 C120 10 220 0 330 22 S520 62 600 50 L600 62 L0 62 Z" fill="#fff"/>
        <path d="M0 52 C120 10 220 0 330 22 S520 62 600 50" fill="none" stroke="#2ab8f2" stroke-width="4"/>
      </svg>
    </header>
    <section class="intro">
      <div class="eyebrow">Why WebQuilt</div>
      <h1>Harness the power of AI to instantly build<br>your amazing FREE website today!</h1>
    </section>
    <div class="illustration" role="img" aria-label="Line illustration of a person working on a laptop with an AI thought bubble"></div>
    <div class="copy">
      <p>WebQuilt is the world’s first website builder that builds professional, high - quality websites in seconds!</p>
      <p>Say goodbye to the traditional expensive and time - conuming methods of getting your business online.</p>
    </div>
    <a class="btn">Generate free site now</a>
    <footer class="footer">
      <div class="brand"><span class="brand-mark"></span>WebQuilt</div>
      <div class="tagline">Lorem Ipsum is text simply dummy Ipsum</div>
      <div class="social"><span></span><span></span><span></span><span></span></div>
      <div class="rule"></div>
      <div class="legal"><span>@2023 WebQuilt. All Rights Reserved.</span><span>Unsubscribe</span></div>
    </footer>
  </div>
</div>
</body>
</html>
```